依頼詳細
メルマガ登録用のランディングページをお願いします。概要に書かせて頂いた通り、
変わるきっかけが欲しいけどなかなか行動できない方たちが、
作成していただいたLPから可能性を感じて、
ここなら変われるかも知れないと期待感が湧きでるような、
未来を想像して興奮してしまうような感じでお願いします。
ファーストインプレッションは大事にしたいです。

スマホとPCのどちらでも見られるような大きさでお願いします。
サイトURL
http://hanabira-tsumugi.com/lp/
ページ数
1ページ
希望イメージ
シンプル 複雑
単色 カラフル
暗い 明るい
日常 高級
遊び心 厳粛
未来的 伝統的
女性的 男性的
希望する色
納品ファイル
補足説明
作成していただいたLP内の文章などあとで、
wordpressで編集できるようにしていただきたいです。
初めての依頼なので、作成していただく時点で不明点などあれば、
すぐに追記させていただきます!!!
提案の締め切りを1日のばしました。
みなさまのご提案楽しみにしております。
■ 選んだ理由

ファーストインパクトが気に入りました。

■ 提案者全員のお礼・コメント

初心者の提案でも丁寧に提案していただきみなさまありがとうございます。

```html
<!DOCTYPE html>
<html lang="ja">
<head>
<meta charset="utf-8">
<title>モテない男子ご注意｜無料登録</title>
<link rel="stylesheet" href="https://fonts.googleapis.com/css2?family=Noto+Serif+JP:wght@500;700;900&family=Noto+Sans+JP:wght@400;500;700&display=swap">
<style>
:root{
  --navy:#1d3352;
  --navy-deep:#132440;
  --navy-soft:#2c4a72;
  --orange:#f29a1f;
  --orange-deep:#e0701a;
  --red:#c9261c;
  --gold:#d89a2a;
  --ink:#222;
  --paper:#f4f4f2;
  --cream:#fbf3d6;
  --white:#fff;
}
*{margin:0;padding:0;box-sizing:border-box}
html,body{width:1200px;height:5052px;overflow:hidden}
body{position:relative;background:var(--white);font-family:"Noto Sans JP",sans-serif;color:var(--ink)}
.abs{position:absolute}
.serif{font-family:"Noto Serif JP",serif}

/* hero */
.hero{left:0;top:0;width:1200px;height:1160px;background:linear-gradient(180deg,#fbfbfa 0%,#eceef1 45%,#cfd6df 68%,var(--navy) 70%,var(--navy-deep) 100%)}
.hero-photo{left:720px;top:0;width:480px;height:860px;background:linear-gradient(180deg,#e9e9e7 0%,#3a3b40 55%,#24252a 100%)}
.hero-silhouette{left:112px;top:380px;width:270px;height:560px;background:linear-gradient(180deg,#d9c2a4 0%,#c6a985 100%);border-radius:120px 120px 20px 20px;opacity:.75}
.warning-tag{left:180px;top:40px;width:400px;height:76px;background:linear-gradient(180deg,var(--orange),var(--orange-deep));color:var(--white);font-size:36px;font-weight:700;display:flex;align-items:center;justify-content:center;transform:skewX(-8deg);box-shadow:0 4px 0 #b85d14;white-space:nowrap}
.headline{left:170px;top:230px;font-size:70px;font-weight:900;line-height:1.3;color:var(--navy-deep);white-space:nowrap}
.headline .l2{display:block;padding-left:150px}
.headline em{font-style:normal;color:var(--red)}
.produce{left:400px;top:462px;font-size:40px;font-weight:700;line-height:1.4;color:var(--white);-webkit-text-stroke:1.5px var(--red);paint-order:stroke fill;text-shadow:0 0 6px var(--red);white-space:nowrap}
.nanto{left:190px;top:872px;background:var(--orange-deep);color:var(--white);font-size:30px;font-weight:700;padding:2px 20px;transform:rotate(-8deg);z-index:2;white-space:nowrap}
.ribbon{left:160px;top:928px;width:960px;height:150px;background:linear-gradient(90deg,rgba(255,255,255,.7),var(--white) 20%,var(--white) 80%,rgba(255,255,255,.7));display:flex;flex-direction:column;justify-content:center;align-items:center}
.ribbon p{font-size:36px;font-weight:700;line-height:1.35;color:var(--navy-deep);white-space:nowrap}
.ribbon strong{color:var(--orange-deep);font-size:48px}

/* form */
.form-area{left:0;top:1160px;width:1200px;height:560px;background:var(--navy)}
.form-card{left:140px;top:1200px;width:920px;height:480px;background:linear-gradient(180deg,#ffffff,#f3efe6);border:2px solid #d8d2c2}
.form-title{left:0;top:1236px;width:1200px;text-align:center;font-size:42px;font-weight:700}
.form-title span{border-bottom:4px solid var(--red);padding:0 30px 8px}
.form-label{left:240px;font-size:34px;font-weight:700}
.form-input{left:420px;width:560px;height:58px;background:var(--white);border:2px solid #bbb;border-radius:4px}
.submit{left:390px;top:1520px;width:420px;height:100px;background:linear-gradient(180deg,#f8c36a,var(--orange) 55%,var(--orange-deep));border-radius:8px;color:var(--white);font-size:28px;font-weight:700;display:flex;align-items:center;justify-content:center;gap:14px;box-shadow:0 4px 0 #b85d14;white-space:nowrap}
.submit i{width:44px;height:30px;background:#fff3d8;display:block;transform:rotate(-10deg)}
.strip{left:0;top:1720px;width:1200px;height:40px;background:var(--navy-soft)}

/* checklist */
.checklist-area{left:0;top:1760px;width:1200px;height:1040px;background:var(--paper)}
.check-banner{left:40px;top:1800px;width:1120px;height:150px;background:var(--navy);transform:skewX(-6deg);box-shadow:0 6px 0 #0c1a2e}
.check-banner-text{left:70px;top:1810px;font-size:48px;font-weight:900;color:var(--white);line-height:1.3;white-space:nowrap}
.check-banner-text b{font-size:70px;color:var(--orange)}
.checklist{left:70px;top:1996px;width:1060px;list-style:none}
.checklist li{height:68px;display:flex;align-items:center;gap:18px;font-size:31px;font-weight:500;border-bottom:2px dashed #c9c9c9;white-space:nowrap}
.checklist li em{font-style:normal;color:var(--orange-deep);font-weight:700;font-size:36px}
.checklist svg{flex:none}

/* mote season */
.wave{left:0;top:2800px;width:1200px;height:240px}
.season-title{left:0;top:3060px;width:1200px;text-align:center;font-size:50px;font-weight:900;color:var(--gold)}
.season-text{left:80px;top:3190px;width:560px;font-size:31px;line-height:1.85;font-weight:500}
.season-photo{left:600px;top:3160px;width:600px;height:840px;background:linear-gradient(180deg,#f4f4f4 0%,#cfd0d2 40%,#1f2430 70%,#d9d9d9 100%)}

/* mindset */
.mind-area{left:0;top:4020px;width:1200px;height:1032px;background:linear-gradient(180deg,var(--navy-soft),var(--navy) 40%,var(--navy-deep))}
.mind-title{left:0;top:4080px;width:1200px;text-align:center;font-size:54px;font-weight:900;color:#ffe27a}
.mind-photo{left:70px;top:4220px;width:460px;height:520px;background:radial-gradient(circle at 50% 40%,#f3e6dc,#d8c3b6 55%,rgba(44,74,114,0) 72%)}
.mind-text{left:570px;top:4230px;width:580px;font-size:30px;line-height:1.75;color:var(--white)}
.mind-text p+p{margin-top:30px}
.note{left:120px;top:4760px;width:960px;height:292px;background:var(--cream);border-top:10px solid var(--orange);padding:40px 60px;font-size:31px;line-height:1.9;font-weight:500;color:var(--navy-deep);white-space:nowrap}
</style>
</head>
<body>

<div class="abs hero"></div>
<div class="abs hero-photo" role="img" aria-label="スーツ姿の男性モデルの写真"></div>
<div class="abs hero-silhouette" role="img" aria-label="変身前の男性のシルエット"></div>
<div class="abs warning-tag">モテない男子ご注意</div>
<h1 class="abs headline serif">あなたに<em>「大逆転」</em>が<span class="l2">起こるかも</span></h1>
<p class="abs produce serif">現役モデルが<br>あなたをプロデュース！</p>
<div class="abs ribbon serif">
  <p>たった1ヶ月で見知らぬ<strong>5人の女性</strong>を虜にする</p>
  <p>方法を伝授します。</p>
</div>
<div class="abs nanto serif">なんと</div>

<div class="abs form-area"></div>
<div class="abs form-card"></div>
<h2 class="abs form-title serif"><span>いますぐ無料で登録</span></h2>
<label class="abs form-label serif" style="top:1340px">お名前</label>
<div class="abs form-input" style="top:1334px"></div>
<label class="abs form-label serif" style="top:1436px">E-Mail</label>
<div class="abs form-input" style="top:1430px"></div>
<div class="abs submit"><i></i>入力が完了したらクリック</div>
<div class="abs strip"></div>

<div class="abs checklist-area"></div>
<div class="abs check-banner"></div>
<h2 class="abs check-banner-text serif">モテない人生から<br>　　　<b>180°</b>人生を変えてみませんか！</h2>
<ul class="abs checklist">
  <li><svg width="30" height="30" viewBox="0 0 30 30"><rect x="2" y="2" width="26" height="26" fill="#fff" stroke="#1d3352" stroke-width="3"/><path d="M7 15l6 6 11-13" fill="none" stroke="#1d3352" stroke-width="4"/></svg>自分に<em>自信がなく</em>、自分を<em>変えたい</em>人</li>
  <li><svg width="30" height="30" viewBox="0 0 30 30"><rect x="2" y="2" width="26" height="26" fill="#fff" stroke="#1d3352" stroke-width="3"/><path d="M7 15l6 6 11-13" fill="none" stroke="#1d3352" stroke-width="4"/></svg>一緒に恋愛活動を頑張っていける<em>仲間が欲しい</em>人</li>
  <li><svg width="30" height="30" viewBox="0 0 30 30"><rect x="2" y="2" width="26" height="26" fill="#fff" stroke="#1d3352" stroke-width="3"/><path d="M7 15l6 6 11-13" fill="none" stroke="#1d3352" stroke-width="4"/></svg>女性といろいろな場所で<em>出会う方法</em>を知りたい人</li>
  <li><svg width="30" height="30" viewBox="0 0 30 30"><rect x="2" y="2" width="26" height="26" fill="#fff" stroke="#1d3352" stroke-width="3"/><path d="M7 15l6 6 11-13" fill="none" stroke="#1d3352" stroke-width="4"/></svg><em>友達から恋人</em>に<em>発展</em>する方法を知りたい人</li>
  <li><svg width="30" height="30" viewBox="0 0 30 30"><rect x="2" y="2" width="26" height="26" fill="#fff" stroke="#1d3352" stroke-width="3"/><path d="M7 15l6 6 11-13" fill="none" stroke="#1d3352" stroke-width="4"/></svg>出会った女性と<em>一瞬で仲良く</em>なれる方法を知りたい人</li>
  <li><svg width="30" height="30" viewBox="0 0 30 30"><rect x="2" y="2" width="26" height="26" fill="#fff" stroke="#1d3352" stroke-width="3"/><path d="M7 15l6 6 11-13" fill="none" stroke="#1d3352" stroke-width="4"/></svg><em>自分に合ったやり方</em>を知りたい人</li>
  <li><svg width="30" height="30" viewBox="0 0 30 30"><rect x="2" y="2" width="26" height="26" fill="#fff" stroke="#1d3352" stroke-width="3"/><path d="M7 15l6 6 11-13" fill="none" stroke="#1d3352" stroke-width="4"/></svg><em>恋人</em>までいけず、<em>いい人止まり</em>で終わってしまう人</li>
  <li><svg width="30" height="30" viewBox="0 0 30 30"><rect x="2" y="2" width="26" height="26" fill="#fff" stroke="#1d3352" stroke-width="3"/><path d="M7 15l6 6 11-13" fill="none" stroke="#1d3352" stroke-width="4"/></svg><em>タイプ別</em>の落とし方を知りたい人</li>
  <li><svg width="30" height="30" viewBox="0 0 30 30"><rect x="2" y="2" width="26" height="26" fill="#fff" stroke="#1d3352" stroke-width="3"/><path d="M7 15l6 6 11-13" fill="none" stroke="#1d3352" stroke-width="4"/></svg><em>モチベーション</em>が上がらず、すぐに諦めてしまう人</li>
  <li><svg width="30" height="30" viewBox="0 0 30 30"><rect x="2" y="2" width="26" height="26" fill="#fff" stroke="#1d3352" stroke-width="3"/><path d="M7 15l6 6 11-13" fill="none" stroke="#1d3352" stroke-width="4"/></svg><em>本当に効果がある</em>のかわからないし<em>信用</em>できない人</li>
</ul>

<svg class="abs wave" viewBox="0 0 1200 240" preserveAspectRatio="none"><rect width="1200" height="240" fill="#fff"/><path d="M0 0H1200V150Q600 260 0 150Z" fill="#1d3352"/></svg>
<h2 class="abs season-title serif">あなたの人生のモテ期を永遠に！！</h2>
<div class="abs season-photo" role="img" aria-label="床に座り込んで落ち込む男性の写真"></div>
<div class="abs season-text">
  <p>たった一度きりの人生。<br>多くの女性と出会い仲良くしたい理想の自分に変えたいなら</p>
  <p style="margin-top:30px">自分がもし芸能人だったら。。。<br>自分がものすごいイケメンだったら。。。<br>鏡を見ては憂鬱になる一方、周りのイケメンを見ては自分とは住む世界が違うんだ。なんて思っていませんか？</p>
</div>

<div class="abs mind-area"></div>
<h2 class="abs mind-title serif">恋愛テクニックよりも重要な恋愛マインド</h2>
<div class="abs mind-photo" role="img" aria-label="手を差し伸べるイメージ写真"></div>
<div class="abs mind-text">
  <p>あなたは女性からの拒絶、否定を恐れ、どんどんと自分の殻に閉じこもってしまっていませんか。</p>
  <p>自分の殻に閉じこもるあまりいつのまにか女性に対して恐怖心を抱き一切の行動が出来ない状態なのであれば、今までのモテ方とは全く逆の発想でモテる力をつけて行くプログラムを知りたくないですか。</p>
</div>
<div class="abs note">このお手紙ではその方法を全てお伝えしていますので、<br>今直ぐに読み進めて下さい。<br>恋愛の考え方の重要性を理解している真のモテ男になる為に</div>

</body>
</html>
```